Label for Sugar Scrub, sugar peeling

We need a label for a SugarScrub can. We produce both sugar and salt scrubs for B2C and B2B. The market is more dominated by women, but we also want to bring the men on board. In addition to the logo as a font may also fit a picture, a silhouette o.ä. be introduced. Overall, it should be structured rather clearly, more masculine than too flowery and simply modern. It may be multicolored, but not too colorful. The high quality should be highlighted by the design, as it is more in the upper price segment settled. Since we work only with natural "100% Organic" ingredients, it may also be colored accordingly. There will be different fragrances. As an example files, I would attach rosemary lemon. But it should also be a variety of compositions austere nature, other fruits such as grapefruit, lime, etc. are produced. The dimensions of the product label are 25 x 250 mm (WxH). A round logo for the lid is to be designed with 78mm diameter matching, but only logo, the image of the scent direction and the fragrance name or the words "Sugar Scrub" included. As a box will serve, inter alia, a bamboo can, but also a semi-transparent plastic can be used. The sale takes place both online, as in beauty salons and hotels as a product in the exhibition. The label is white or transparent for the plastic box, but only transparent for the bamboo box. In the course I can gladly send the company logo by e-mail. At first I do not want to give away too much. The sample texts for the label are included in the appendix. All in all, however, I would like to give free rein to the freedom of design and not limit too much. Questions can be asked at any time, I will try to answer as soon as possible. However, the project should be open until 16.04. reasonably stand. Otherwise, I can probably only from 18.04. reply.

Target Market(s)

Target market are end users, B2B customers (sauna operators, hotels) and customers of beauty salons.

Font styles to use
Sans Serif

Requirements
Must have
• The three blocks "Ingredients, Logo, Application Recommendation" must be clearly arranged. My logo has the colors (RGB): 63, 148,167 4, 4, 4 152, 152, 152
Nice to have
• It would be nice if it has a rather clear design that appeals to men as well. Possibly. Maybe just by a different color choice could be minted on women.
Should not have

```html
<!DOCTYPE html>
<html lang="de">
<head>
<meta charset="utf-8">
<title>Verdalis – Zuckerpeeling Rosmarin-Zitrone</title>
<link rel="stylesheet" href="https://fonts.googleapis.com/css2?family=Montserrat:wght@400;500;600;700&family=PT+Sans+Narrow:wght@400;700&display=swap">
<style>
  :root {
    --brand-teal: #3f94a7;
    --lid-ring: #34808f;
    --ink: #040404;
    --text-grey: #989898;
    --stage-dark: #262626;
    --paper: #ffffff;
    --badge-green: #6aab45;
    --badge-light: #8fc26d;
    --herb-green: #7aa35a;
    --lemon: #f1dc6a;
  }
  * { margin: 0; padding: 0; box-sizing: border-box; }
  html, body { width: 1200px; height: 794px; overflow: hidden; }
  body {
    position: relative;
    background: var(--paper);
    font-family: "Montserrat", sans-serif;
  }
  .stage-top {
    position: absolute; left: 0; top: 0; width: 1200px; height: 498px;
    background: linear-gradient(180deg, #eef0f0 0%, #f7f8f8 18%, #ffffff 34%);
  }
  .stage-bottom {
    position: absolute; left: 0; top: 498px; width: 1200px; height: 296px;
    background: var(--stage-dark);
  }

  /* Lid sticker */
  .lid {
    position: absolute; left: 789px; top: 317px; width: 242px; height: 242px;
    border-radius: 50%;
    background: var(--brand-teal);
    border: 5px solid var(--lid-ring);
    color: var(--paper);
    text-align: center;
  }
  .lid__brand {
    position: absolute; left: 0; right: 0; top: 70px;
    font-size: 29px; font-weight: 400; letter-spacing: -0.5px;
  }
  .lid__rule {
    position: absolute; left: 30px; right: 30px; height: 1px; background: var(--paper);
  }
  .lid__rule--top { top: 117px; }
  .lid__rule--bottom { top: 146px; }
  .lid__product {
    position: absolute; left: 0; right: 0; top: 121px;
    font-size: 19px; font-weight: 600; letter-spacing: 0.4px;
  }
  .lid__scent {
    position: absolute; left: 0; right: 0; top: 154px;
    font-size: 10px; font-weight: 600; letter-spacing: 1.6px;
  }

  .size-note {
    position: absolute; left: 35px; top: 566px;
    color: var(--paper); font-size: 10px; font-weight: 600;
  }

  /* Front label strip */
  .label {
    position: absolute; left: 32px; top: 588px; width: 1140px; height: 113px;
    background: var(--paper);
  }
  .label__block {
    position: absolute; white-space: nowrap;
    font-family: "PT Sans Narrow", sans-serif; font-weight: 700;
    font-size: 10.5px; line-height: 13.7px; color: var(--text-grey);
  }
  .label__ingredients { left: 66px; top: 10px; }
  .label__ingredients p + p { margin-top: 8px; }
  .label__usage { left: 771px; top: 25px; }

  .label__badge { position: absolute; left: 390px; top: 27px; }
  .label__brand {
    position: absolute; left: 495px; top: 14px;
    font-size: 22px; font-weight: 400; color: var(--ink); letter-spacing: -0.3px;
  }
  .label__product {
    position: absolute; left: 484px; top: 53px;
    font-size: 14px; font-weight: 700; color: var(--brand-teal); letter-spacing: 0.3px;
  }
  .label__scent-band {
    position: absolute; left: 465px; top: 77px; width: 160px; height: 19px;
    background: var(--ink); color: var(--paper);
    font-size: 9.5px; font-weight: 600; letter-spacing: 1.4px;
    line-height: 19px; padding-left: 12px; white-space: nowrap;
  }
  .label__illustration {
    position: absolute; left: 630px; top: 8px; width: 90px; height: 98px;
    border-radius: 8px 50% 50% 8px;
    background: linear-gradient(120deg, var(--herb-green) 0%, #a9c27a 45%, var(--lemon) 75%, #f6e9a4 100%);
  }
</style>
</head>
<body>
  <div class="stage-top"></div>
  <div class="stage-bottom"></div>

  <div class="lid">
    <div class="lid__brand">Verdalis</div>
    <div class="lid__rule lid__rule--top"></div>
    <div class="lid__product">ZUCKERPEELING</div>
    <div class="lid__rule lid__rule--bottom"></div>
    <div class="lid__scent">ROSMARIN-ZITRONE</div>
  </div>

  <div class="size-note">25 x 250 mm</div>

  <div class="label">
    <div class="label__block label__ingredients">
      <p>Zutaten: Lorem ipsum dolor sit amet, consetetur sadipscing elitr, sed<br>diam nonumy eirmod<br>tempor invidunt ut labore et dolore magna aliquyam erat</p>
      <p>360 gr Netto<br>MHD: 12/2019<br>Recycling Zeichen, Kunststoffbezeichnung</p>
    </div>

    <svg class="label__badge" width="78" height="78" viewBox="0 0 78 78" role="img" aria-label="Siegel für natürliche Zutaten">
      <circle cx="39" cy="39" r="37" fill="var(--badge-green)"/>
      <circle cx="39" cy="39" r="29" fill="var(--badge-light)"/>
    </svg>

    <div class="label__brand">Verdalis</div>
    <div class="label__product">ZUCKERPEELING</div>
    <div class="label__scent-band">ROSMARIN-ZITRONE</div>
    <div class="label__illustration" role="img" aria-label="Rosmarinzweig und Zitronenscheibe"></div>

    <div class="label__block label__usage">
      Anwendungshinweis: Nach dem Duschen oder der Sauna anwenden. Haut<br>von überschüssigem Wasser befreien und Peeling kreisend auf die noch<br>feuchte Haut kreisend einmassieren, bis es sich aufgelöst hat. Warm<br>abduschen und Haut mit Handtuch trocken tupfen.
    </div>
  </div>
</body>
</html>
```